Collectible Card Trading Company ~ Tin and Amber Collectibles

Business card design using the attached images as a reference point. The color pallet is the color choice I prefer. If you have any way of improving on the design that would be appreciated. This will be used as an insert for product shipments as well as at vexafest and other collectible trade shows so it needs to be eye catching and memorable. Anything that you can do to make my business POP with this business card would be appreciated.

Target Market(s)

Collectible card purchasers primarily but all collectors ingeneral

Industry/Entity Type

Retail

Contact Information for Business Card

Details are included on the provided images

Colors

Designer to choose colors to be used in the design.

Requirements
Must have
• Bold design
Nice to have
• N/A
Should not have
• N/A

```html
<!DOCTYPE html>
<html lang="en">
<head>
<meta charset="utf-8">
<title>Tin &amp; Amber Co. — Business Card</title>
<link rel="stylesheet" href="https://fonts.googleapis.com/css2?family=Oswald:wght@300;400;700&family=Ubuntu:wght@700&display=swap">
<style>
  :root {
    --stage: #2a2a2c;
    --slate: #30333b;
    --amber: #b97e3b;
    --amber-deep: #a86e30;
    --amber-light: #c08543;
    --ink: #33343a;
    --cream: #f6ead6;
  }
  * { box-sizing: border-box; margin: 0; padding: 0; }
  html, body { width: 1200px; height: 900px; overflow: hidden; background: var(--stage); }
  .canvas { position: relative; width: 1200px; height: 900px; }

  .card {
    position: absolute;
    width: 700px; height: 400px;
    border-radius: 28px;
    overflow: hidden;
    box-shadow: 0 18px 40px rgba(0,0,0,0.5);
  }
  .card--front { left: 110px; top: 50px; background: var(--slate); color: var(--amber); }
  .card--back {
    left: 390px; top: 450px; color: var(--ink);
    background: linear-gradient(135deg, var(--amber-deep) 0%, var(--amber) 55%, var(--amber-light) 100%);
  }

  /* Brand lockup */
  .lockup { position: absolute; display: grid; justify-items: center; }
  .card--front .lockup { left: 50%; top: 58px; transform: translateX(-50%); width: 460px; }
  .card--back .lockup { right: 34px; top: 30px; width: 300px; }

  .lockup__name {
    font-family: "Oswald", sans-serif; font-weight: 700;
    font-size: 50px; letter-spacing: 1px; line-height: 1; white-space: nowrap;
  }
  .card--back .lockup__name { font-size: 32px; }

  .lockup__row {
    display: grid; grid-template-columns: 1fr auto 1fr; align-items: end;
    width: 100%; margin-top: 14px; column-gap: 18px;
  }
  .card--back .lockup__row { margin-top: 9px; column-gap: 12px; }

  .lockup__meta {
    font-family: "Ubuntu", sans-serif; font-weight: 700; font-size: 20px; line-height: 1;
  }
  .lockup__meta--est { justify-self: end; }
  .lockup__meta--year { justify-self: start; align-self: start; font-size: 16px; letter-spacing: 1px; }
  .card--back .lockup__meta { font-size: 13px; }
  .card--back .lockup__meta--year { font-size: 11px; }

  .lockup__mark {
    width: 150px; height: 130px; border-radius: 46% 46% 40% 40%;
    background: radial-gradient(circle at 50% 45%, currentColor 0%, currentColor 38%, transparent 72%);
    opacity: 0.55;
  }
  .card--back .lockup__mark { width: 96px; height: 84px; opacity: 0.6; }

  .lockup__tagline {
    font-family: "Ubuntu", sans-serif; font-weight: 700; font-size: 22px;
    letter-spacing: 0.5px; margin-top: 12px;
  }
  .card--back .lockup__tagline { font-size: 14px; margin-top: 8px; }

  /* Back side */
  .backdrop-art {
    position: absolute; left: 70px; top: 20px;
    width: 420px; height: 380px; border-radius: 46% 46% 40% 40%;
    background: radial-gradient(circle at 50% 48%, rgba(120,75,30,0.28) 0%, rgba(120,75,30,0.16) 45%, transparent 72%);
  }

  .holder { position: absolute; left: 40px; top: 34px; }
  .holder__name { font-family: "Oswald", sans-serif; font-weight: 700; font-size: 34px; color: var(--ink); line-height: 1.1; }
  .holder__title { font-family: "Oswald", sans-serif; font-weight: 300; font-size: 24px; color: var(--cream); line-height: 1.2; }

  .contact {
    position: absolute; left: 40px; list-style: none;
    font-family: "Oswald", sans-serif; font-weight: 300; font-size: 21px;
    color: var(--cream); line-height: 1.4;
  }
  .contact--personal { top: 142px; }
  .contact--online { top: 236px; }
  .contact li { display: flex; align-items: center; gap: 10px; }
  .contact svg { width: 18px; height: 18px; flex: none; }
  .badge { width: 16px; height: 16px; border-radius: 4px; background: var(--ink); flex: none; margin: 0 1px; }
</style>
</head>
<body>
<main class="canvas">

  <section class="card card--front" aria-label="Card front">
    <div class="lockup">
      <div class="lockup__name">Tin &amp; Amber Co.</div>
      <div class="lockup__row">
        <span class="lockup__meta lockup__meta--est">est.</span>
        <span class="lockup__mark" role="img" aria-label="Brand mark area"></span>
        <span class="lockup__meta lockup__meta--year">2016</span>
      </div>
      <div class="lockup__tagline">Cards &amp; Collectibles</div>
    </div>
  </section>

  <section class="card card--back" aria-label="Card back">
    <div class="backdrop-art" role="img" aria-label="Faint large brand mark backdrop area"></div>

    <div class="lockup">
      <div class="lockup__name">Tin &amp; Amber Co.</div>
      <div class="lockup__row">
        <span class="lockup__meta lockup__meta--est">est.</span>
        <span class="lockup__mark" role="img" aria-label="Brand mark area"></span>
        <span class="lockup__meta lockup__meta--year">2016</span>
      </div>
      <div class="lockup__tagline">Cards &amp; Collectibles</div>
    </div>

    <div class="holder">
      <div class="holder__name">Marcus Thole Jr.</div>
      <div class="holder__title">Chief Collector</div>
    </div>

    <ul class="contact contact--personal">
      <li>
        <svg viewBox="0 0 16 16" aria-hidden="true"><rect x="1" y="3" width="14" height="10" rx="1.5" fill="var(--ink)"/><path d="M1.5 4l6.5 5 6.5-5" stroke="var(--cream)" stroke-width="1.2" fill="none"/></svg>
        marcus@tinandamberco.com
      </li>
      <li>
        <svg viewBox="0 0 16 16" aria-hidden="true"><path d="M8 1a5 5 0 0 0-5 5c0 4 5 9 5 9s5-5 5-9a5 5 0 0 0-5-5z" fill="var(--ink)"/><circle cx="8" cy="6" r="2" fill="var(--amber)"/></svg>
        pinecrest, colorado
      </li>
    </ul>

    <ul class="contact contact--online">
      <li>
        <svg viewBox="0 0 16 16" aria-hidden="true"><circle cx="8" cy="8" r="7" fill="var(--ink)"/><g stroke="var(--amber)" stroke-width="1" fill="none"><ellipse cx="8" cy="8" rx="3" ry="7"/><path d="M1 8h14M2.5 4.5h11M2.5 11.5h11"/></g></svg>
        www.tinandamberco.com
      </li>
      <li><span class="badge"></span>@tinandamberco</li>
      <li><span class="badge"></span>@Tin_and_amber</li>
      <li><span class="badge"></span>@www.bidhollow.com/str/tinandamberco</li>
    </ul>
  </section>

</main>
</body>
</html>
```